Creative label for amber glass candle jar.

We are a candle company. Our products are handmade by us and natural. We are looking for something minimalistic and unique. We need a label for our candle jars (amber glass with black lid). Our current label doesn't match these requirements. We would like our products to be stocked in London shop, therefore design has to be up to a high standard. Jar specification Diameter (mm) 65 Height without cap (mm) 80. We want the new design to be different from the current one. It's just a guide for wording.
We should be able adjust the label, to change scent name.
Our scents are
*Coconut & Vanilla
*Lavender
*Bergamot
*Italian Garden
*Hygge
*Eucalyptus & Peppermint
*Coffee
*Cedarwood & Juniperberry
To know more about us, visit our website www.wrenfieldcandles.com or instagram.com/wrenfieldcandles
Good luck!
Industry/Entity Type
It Company
Colors
Designer to choose colors to be used in the design.
Requirements
Must have
- * I have attached two of our logos, label design must include one of them.
- *has to mention that it's made in London
- *has to say that candle is natural/made with essential oils
- *has to have scent name and No. on it..
- Label can be vertical or horizontal, but has to be square/rectangular,.
Should not have
- Label should not be round

```html
<!DOCTYPE html>
<html lang="en">
<head>
<meta charset="utf-8">
<title>wrenfield — candle label redesign</title>
<link rel="stylesheet" href="https://fonts.googleapis.com/css2?family=Share+Tech+Mono&display=swap">
<style>
  :root {
    --wood-light: #d9bfa1;
    --wood-mid: #c5a282;
    --wood-dark: #9c7a5f;
    --ink: #111111;
    --label-green: #1f5b58;
    --label-text: #7fb38c;
    --label-shadow: rgba(10, 30, 28, 0.55);
  }
  * { margin: 0; padding: 0; box-sizing: border-box; }
  html, body { width: 695px; height: 1200px; overflow: hidden; }
  body {
    position: relative;
    font-family: "Share Tech Mono", monospace;
    color: var(--ink);
  }
  .wood-backdrop {
    position: absolute; inset: 0;
    background: linear-gradient(90deg,
      var(--wood-light) 0%, var(--wood-mid) 12%, var(--wood-dark) 16%,
      var(--wood-mid) 20%, var(--wood-light) 45%, var(--wood-mid) 70%,
      var(--wood-light) 100%);
  }
  .sheet-header { position: absolute; left: 60px; top: 40px; }
  .sheet-title { font-size: 64px; line-height: 1; letter-spacing: 2px; }
  .sheet-subtitle { margin: 14px 0 0 66px; font-size: 21px; letter-spacing: 1.5px; }
  .sheet-number { margin-top: 20px; font-size: 19px; letter-spacing: 1.5px; }

  .label {
    position: absolute; left: 200px; width: 306px; height: 268px;
    background: var(--label-green);
    box-shadow: 4px 6px 8px var(--label-shadow);
    color: var(--label-text);
    text-align: center;
  }
  .label--coconut { top: 240px; }
  .label--coffee { top: 538px; }
  .label--lavender { top: 838px; }
  .scent-name {
    position: absolute; left: 0; right: 0; top: 18px;
    font-size: 38px; line-height: 40px; letter-spacing: 2px;
    text-shadow: 3px 4px 4px var(--label-shadow);
  }
  .brand-name { position: absolute; left: 0; right: 0; top: 128px; font-size: 20px; letter-spacing: 1px; }
  .brand-note { position: absolute; left: 0; right: 0; top: 154px; font-size: 8px; line-height: 10px; }
  .scent-number {
    position: absolute; left: 0; right: 0; top: 188px;
    font-size: 60px; line-height: 60px;
    text-shadow: 3px 4px 4px var(--label-shadow);
  }
</style>
</head>
<body>
  <div class="wood-backdrop" role="img" aria-label="Weathered wooden plank surface in light tan tones"></div>

  <header class="sheet-header">
    <h1 class="sheet-title">wrenfield</h1>
    <p class="sheet-subtitle">candle label redesign</p>
    <p class="sheet-number">design 03</p>
  </header>

  <section class="label label--coconut">
    <h2 class="scent-name">coconut &amp;<br>vanilla</h2>
    <p class="brand-name">wrenfield</p>
    <p class="brand-note">homemade in london using<br>natural essential oils</p>
    <p class="scent-number">01</p>
  </section>

  <section class="label label--coffee">
    <h2 class="scent-name">coffee</h2>
    <p class="brand-name">wrenfield</p>
    <p class="brand-note">homemade in london using<br>natural essential oils</p>
    <p class="scent-number">07</p>
  </section>

  <section class="label label--lavender">
    <h2 class="scent-name">lavender</h2>
    <p class="brand-name">wrenfield</p>
    <p class="brand-note">homemade in london using<br>natural essential oils</p>
    <p class="scent-number">02</p>
  </section>
</body>
</html>
```